Come crowdsource a Web Design for a brazilian crowdsource Startup!

> NAME OF OUR STARTUP:
Mundaleo

> DESCRIPTION OF OUR STARTUP:
We are a crowdsourcing startup in Brazil providing consultancy and technology to support other companies to crowdsource their projects.
We also operate doing big crowdsource campaings related to polemic subjects in Brazil.

> WHAT ARE OUR TARGET AUDIENCE?
Our target audience are young people around 20-35 years old.
Generation Y (Millennial Generation)

> WHAT IS OUR INDUSTRY?
Internet, web

> WHAT DO WE NEED?
We need a Web Design for our first site.

We need 5 pages:
- Home
- What is Crowdsourcing?
- Solutions
- About Us
- Blog
- A box for the "Contact" tab (this is not a page)

Please, find attached a Layout Sketch of what I've imagined.

Lets talk about the sketch:
Well, first of all, it's a SKETCH, so you don't have to send proposals exactly as the sketch. The sketch is just to show how I've imagined the ditribution of the content boxes. For example, the menu bar doesnt need to be a rectangle exactly like the sketch, but, I would like to have the menu on the right side of the logo. Also, you will see that the boxes are all squeezed, of course I dont want them soo squeezed! Again, its juust a SKETCH!

About the images on the sketch:
IMG1 - Some nice and simple image related to collectivity or related to crowdsourcing or maybe use our O logo.

IMG2 - Some simple and creative image related to Consultancy. It doesnt need to be so obvious.

IMG3 - Some simple and creative image related to Web 2.0 Software Technology. It doesnt need to be so obvious.

IMG4 - Some simple and creative image related to a full package of Consultancy + Technology. It doesnt need to be so obvious.

IMG5 - Some nice and simple image related to collectivity or related to crowdsourcing.

IMG6 - Some nice and simple image related to Ideation. Maybe a light bulb? I dont know, be creative!

IMG7 - Some nice and simple image related to Crowdlabor. I dont know, be creative!

IMG8 - Some nice and simple image related to CrowdFeedback. Maybe a megaphone? A loudspeaker? I dont know, be creative!

IMG9 - Some nice and simple image related to us! Maybe our O logo ? I dont know, be creative!

THE CONTACT SIDE BAR - we need a nice and simple contact side bar. By the way, on the sketch this bar is shown only at the homepage, but when the site becomes real this bar will stay along all the pages.

THE CONTACT BOX - we need a nice and simple contact box.

ABOUT THE COLORS TO USE: we would like some color to our background and titles. We like colors similars to our logo: really light blue ? light green/blue ? light grey ? light orange ? I dont know, you guys knows more about that then me =)

CHATTERBOX SHARE/LIKE BUTTON: We would like a chatterbox share/like button somewhere on the site!

ABOUT THE ATTACHED FILES:

ADDITIONALS:
> The name Mundaleo comes from "collectivity". With our name we want to pass the idea of the collectivity from the crowdsource work model.

> Our communication is directed to the Generation Y.

> Remember, we are a Startup! So we need a modern and simple site, something like the web 2.0 trends. It must be beautiful =)

> We arent a serious company. We are a young and fun company! Please, dont come with old fashionable company sites.

> Be creative =] !

Target Market(s)

Our target audience are young people around 20-35 years old. Generation Y (Millennial Generation)

Industry/Entity Type

Communication

Requirements
Must have
• We need a Web Design for our first site.

We need 5 pages:
- Home
- What is Crowdsourcing?
- Solutions
- About Us
- Blog

ABOUT THE COLORS TO USE: we would like some color to our background and titles. We like colors similars to our logo: really light blue ? light green/blue ? light grey ? light oranges ? I dont know, you guys knows more about that then me =)

Should not have
• Poor/serious/old fashionable designs

```html
<!DOCTYPE html>
<html lang="en">
<head>
<meta charset="utf-8">
<title>Mundaleo – Home</title>
<link rel="stylesheet" href="https://fonts.googleapis.com/css2?family=Oswald:wght@400&family=Open+Sans:wght@400&family=Varela+Round&display=swap">
<style>
  :root {
    --teal: #1fa3b3;
    --teal-dark: #168896;
    --orange: #f7941d;
    --orange-light: #ffa928;
    --nav-divider: #e8851a;
    --page: #f8f8f8;
    --panel: #ececec;
    --text: #5a5a5a;
    --ink: #111;
    --card-tint: #e6f9fc;
    --white: #fff;
  }
  * { margin: 0; padding: 0; box-sizing: border-box; }
  html, body { width: 945px; height: 1200px; overflow: hidden; background: var(--page); }
  body { font-family: "Open Sans", sans-serif; color: var(--text); }
  .page { position: relative; width: 945px; height: 1200px; overflow: hidden; }

  /* Header */
  .top-band { position: absolute; left: 0; top: 0; width: 945px; height: 59px; background: var(--teal); }
  .nav-band { position: absolute; left: 0; top: 59px; width: 945px; height: 53px; background: var(--orange); }
  .logo-tab { position: absolute; left: 0; top: 0; }
  .brand { position: absolute; left: 58px; top: 30px; display: flex; align-items: center; gap: 10px;
    font-family: "Varela Round", sans-serif; font-size: 42px; color: var(--white); line-height: 1; }
  .brand-dot { width: 32px; height: 32px; border-radius: 50%; background: var(--white); flex: none; }
  .phone { position: absolute; left: 430px; top: 13px; font-family: "Oswald", sans-serif; font-size: 24px; color: var(--ink); letter-spacing: .5px; }
  .social { position: absolute; top: 14px; left: 799px; display: flex; gap: 5px; }
  .social span { width: 28px; height: 28px; border-radius: 50%; background: #d7eef2; border: 2px solid #b6dde4; }
  .social span.chatterbox { background: #3b6fc4; border-color: #d7eef2; }

  .main-nav a { position: absolute; top: 68px; height: 35px; line-height: 35px; font-family: "Oswald", sans-serif;
    font-size: 18.5px; color: var(--ink); text-decoration: none; white-space: nowrap; }
  .main-nav a.active { left: 329px; width: 67px; text-align: center; background: var(--teal); color: var(--white); border-bottom: 3px solid var(--teal-dark); }
  .main-nav a.about { left: 431px; }
  .main-nav a.crowd { left: 542px; }
  .main-nav a.solutions { left: 757px; }
  .main-nav a.blog { left: 870px; }
  .nav-divider { position: absolute; top: 68px; width: 1px; height: 35px; background: var(--nav-divider); }

  /* Hero */
  .hero { position: absolute; left: 17px; top: 141px; width: 908px; height: 373px; background: var(--panel);
    box-shadow: 0 14px 12px -12px rgba(0,0,0,.25); }
  .hero-photo { position: absolute; left: 5px; top: 5px; width: 550px; height: 363px;
    background: linear-gradient(135deg, #5d7fd6 0%, #4764b8 50%, #2d3f80 100%); }
  .hero-copy { position: absolute; left: 584px; top: 68px; width: 317px; }
  .hero-title { font-family: "Oswald", sans-serif; font-weight: 400; font-size: 32px; color: var(--teal); line-height: 1; }
  .hero-lead { margin-top: 20px; font-size: 14.5px; color: var(--ink); text-align: justify; line-height: 22px; }
  .hero-text { font-size: 14.5px; color: #777; text-align: justify; line-height: 23px; }
  .btn-more { position: absolute; left: 803px; top: 231px; width: 88px; height: 29px; background: var(--orange-light);
    border-bottom: 2px solid #e07b0a; border-radius: 2px; font-size: 12.5px; color: var(--ink); text-align: center; line-height: 28px; }
  .slider-dots { position: absolute; left: 772px; top: 310px; display: flex; gap: 6px; }
  .slider-dots span { width: 16px; height: 16px; border-radius: 50%; background: #222; }
  .slider-dots span.current { background: var(--teal); }

  /* Welcome */
  .welcome-head { position: absolute; left: 18px; top: 545px; width: 907px; display: flex; align-items: flex-end; gap: 10px; }
  .welcome-title { font-family: "Varela Round", sans-serif; font-size: 24px; color: var(--teal); font-weight: 700; white-space: nowrap; line-height: 30px; }
  .welcome-rule { flex: 1; border-top: 3px dotted #c8c8c8; margin-bottom: 6px; }
  .welcome-text { position: absolute; left: 18px; top: 584px; width: 909px; font-size: 12.4px; line-height: 22.7px; text-align: justify; }
  .read-more { color: var(--teal); font-size: 12.4px; }
  .welcome-more { position: absolute; left: 849px; top: 677px; }

  /* Service cards */
  .card { position: absolute; top: 722px; width: 284px; height: 340px; background: var(--page); border: 1px solid #ddd;
    box-shadow: 0 14px 10px -12px rgba(0,0,0,.3); }
  .card.consultancy { left: 18px; background: var(--card-tint); }
  .card.technology { left: 330px; }
  .card.bundle { left: 643px; }
  .card-photo { width: 282px; height: 196px; background: linear-gradient(135deg, #cfcfcf, #7a7a7a 60%, #3d3d3d); }
  .card.consultancy .card-photo { background: linear-gradient(135deg, #dfe6ee, #8ea0b5 55%, #3d4a5a); }
  .card-title { margin: 8px 0 0 18px; font-family: "Oswald", sans-serif; font-weight: 400; font-size: 19px; color: var(--teal-dark); line-height: 24px; white-space: nowrap; }
  .card-text { margin: 4px 15px 0 18px; font-size: 11.4px; line-height: 18.5px; text-align: justify; color: #333; }
  .card .read-more { position: absolute; right: 15px; bottom: 9px; }

  /* Footer */
  .footer-links { position: absolute; left: 0; top: 1102px; width: 945px; height: 50px; background: var(--teal);
    display: flex; align-items: center; padding-left: 17px; font-size: 12.5px; color: var(--white); }
  .footer-links span.sep { color: #8fd2db; margin: 0 7px; }
  .footer-copy { position: absolute; left: 0; top: 1152px; width: 945px; height: 48px; background: var(--orange);
    padding: 14px 0 0 18px; font-size: 12.5px; color: #fff4e0; }
  .footer-tab { position: absolute; left: 0; top: 0; }
  .footer-brand { position: absolute; left: 712px; top: 1133px; display: flex; align-items: center; gap: 8px;
    font-family: "Varela Round", sans-serif; font-size: 33px; color: var(--white); line-height: 1; white-space: nowrap; }
  .footer-brand .brand-dot { width: 26px; height: 26px; }
</style>
</head>
<body>
<div class="page">

  <header>
    <div class="top-band"></div>
    <div class="nav-band"></div>
    <svg class="logo-tab" width="945" height="120" viewBox="0 0 945 120" aria-hidden="true">
      <path d="M22 59 L40 100 Q46 112 60 112 L290 112 Q304 112 310 100 L332 59 Z" fill="var(--teal)"/>
    </svg>
    <div class="brand"><span class="brand-dot"></span>Mundaleo</div>
    <div class="phone">Call: 555. 210. 4477</div>
    <div class="social" aria-label="Social links">
      <span class="chatterbox" title="chatterbox"></span><span></span><span></span><span></span>
    </div>
    <nav class="main-nav">
      <a class="active">Home</a>
      <span class="nav-divider" style="left:410px"></span>
      <a class="about">About Us</a>
      <span class="nav-divider" style="left:519px"></span>
      <a class="crowd">What is Crowdsourcing?</a>
      <span class="nav-divider" style="left:733px"></span>
      <a class="solutions">Solutions</a>
      <span class="nav-divider" style="left:846px"></span>
      <a class="blog">Blog</a>
    </nav>
  </header>

  <section class="hero">
    <div class="hero-photo" role="img" aria-label="Photo of a person touching a floating speech bubble icon among network figures"></div>
    <div class="hero-copy">
      <h1 class="hero-title">Mundaleo Mission:</h1>
      <p class="hero-lead">Here we tell our mission in a few lines.</p>
      <p class="hero-text">Lorem ipsum dolor sit amet, consectetur adipiscing elit. Vestibulum lectus ante, lacinia eu ultrices non, pellentesque at elit.</p>
    </div>
    <div class="btn-more">More Info »</div>
    <div class="slider-dots"><span class="current"></span><span></span><span></span><span></span><span></span></div>
  </section>

  <div class="welcome-head">
    <h2 class="welcome-title">Welcome to mundaleo</h2>
    <div class="welcome-rule"></div>
  </div>
  <p class="welcome-text">Lorem ipsum dolor sit amet, consectetur adipiscing elit. Nam ultricies lacinia eros, vitae ultricies justo convallis a. Vestibulum ante ipsum primis in faucibus orci luctus et ultrices posuere cubilia Curae; Fusce porta, leo eu condimentum commodo, nunc purus facilisis lectus, quis consequat sem nisl eget elit. In rhoncus mollis sem, convallis fermentum arcu fermentum at. Phasellus consequat condimentum felis, eget rutrum libero hendrerit eget. Sed ullamcorper dictum nulla eu rhoncus. Curabitur tellus massa, congue sodales accumsan eu, sodales sed turpis. Aenean ultrices aliquet ligula sed facilisis.</p>
  <span class="read-more welcome-more">Read more...</span>

  <article class="card consultancy">
    <div class="card-photo" role="img" aria-label="Photo of business people discussing a document"></div>
    <h3 class="card-title">Consultancy</h3>
    <p class="card-text">Lorem ipsum dolor sit amet, consectetur adipiscing elit. Sed in blandit arcu. Phasellus imperdiet dui et libero consectetur euismod. Aliquam quis tortor eros, dapibus</p>
    <span class="read-more">Read more...</span>
  </article>

  <article class="card technology">
    <div class="card-photo" role="img" aria-label="Black and white photo of a technician with a laptop in a server room"></div>
    <h3 class="card-title">TECHONOLOGY</h3>
    <p class="card-text">Lorem ipsum dolor sit amet, consectetur adipiscing elit. Sed in blandit arcu. Phasellus imperdiet dui et libero consectetur euismod. Aliquam quis tortor eros,</p>
    <span class="read-more">Read more...</span>
  </article>

  <article class="card bundle">
    <div class="card-photo" role="img" aria-label="Black and white photo of support staff with headsets at a laptop"></div>
    <h3 class="card-title">CONSULTANCY + TECHNOLOGY</h3>
    <p class="card-text">Lorem ipsum dolor sit amet, consectetur adipiscing elit. Sed in blandit arcu. Phasellus imperdiet dui et libero consectetur euismod. Aliquam quis tortor eros,</p>
    <span class="read-more">Read more...</span>
  </article>

  <footer>
    <nav class="footer-links">
      Home<span class="sep">/</span>About Us<span class="sep">/</span>What is Crowdsourcing?<span class="sep">/</span>Solutions<span class="sep">/</span>Blog
    </nav>
    <div class="footer-copy">Copyright ©2012-2013 All Rights Reserved</div>
    <svg class="footer-tab" width="945" height="1200" viewBox="0 0 945 1200" aria-hidden="true">
      <path d="M681 1152 L690 1182 Q696 1193 710 1193 L892 1193 Q904 1193 910 1182 L926 1130 Q930 1114 912 1114 L700 1114 Q684 1114 681 1130 Z" fill="var(--teal)"/>
    </svg>
    <div class="footer-brand"><span class="brand-dot"></span>Mundaleo</div>
  </footer>

</div>
</body>
</html>
```